Professional modern business card design

A business card for my nutrition business, wanting a professional look, with info clearly visible. Open to using logo colours too.

Would like key info on the front -
logo
my name and qualifications
email
phone number

and just an enlarged logo again / image on the back.

```html
<!DOCTYPE html>
<html lang="en">
<head>
<meta charset="utf-8">
<title>Verde Nutrition – Business Card</title>
<link href="https://fonts.googleapis.com/css2?family=Montserrat:wght@700&family=Source+Sans+3:wght@400;700&display=swap" rel="stylesheet">
<style>
  :root {
    --backdrop: #2b2b2d;
    --card-white: #f7f7f6;
    --navy: #0b2a45;
    --lime: #c8d82a;
    --ink: #0f2c44;
    --divider: #9aa1a8;
    --back-logo: #dfe7ee;
  }
  * { box-sizing: border-box; margin: 0; padding: 0; }
  html, body {
    width: 1200px; height: 900px; overflow: hidden;
    background: var(--backdrop);
    font-family: "Source Sans 3", "Helvetica Neue", Arial, sans-serif;
  }
  .sheet {
    width: 1200px; height: 900px;
    display: flex; flex-direction: column;
    align-items: center; justify-content: center; gap: 56px;
  }
  .card {
    width: 640px; height: 366px;
    border-radius: 26px;
    box-shadow: 0 14px 30px rgba(0,0,0,.45);
    position: relative;
  }
  /* Front */
  .card--front {
    background: var(--card-white);
    display: flex; align-items: center;
  }
  .brand {
    width: 300px;
    display: flex; align-items: center; gap: 12px;
    padding-left: 56px;
  }
  .brand__dot {
    width: 18px; height: 18px; background: var(--lime); flex: none;
  }
  .brand__name {
    font-weight: 700; font-size: 34px; line-height: 1.02;
    color: var(--navy);
  }
  .divider {
    width: 1px; height: 96px; background: var(--divider);
    margin: 0 28px 0 0;
  }
  .details { color: var(--ink); }
  .details__name {
    font-family: "Montserrat", "Helvetica Neue", Arial, sans-serif;
    font-weight: 700; font-size: 19px; letter-spacing: .5px;
    color: var(--navy); text-transform: uppercase;
  }
  .details__role {
    font-size: 15px; color: var(--lime); margin-top: 1px;
  }
  .contact { list-style: none; margin-top: 16px; }
  .contact__item {
    display: flex; align-items: center; gap: 9px;
    font-size: 15px; line-height: 1.5;
  }
  .contact__icon { width: 14px; height: 14px; fill: var(--navy); flex: none; }
  /* Back */
  .card--back {
    background: var(--navy);
    display: flex; align-items: center; justify-content: center;
  }
  .back-brand {
    font-weight: 700; font-size: 60px; line-height: 1;
    color: var(--back-logo); text-align: left;
  }
</style>
</head>
<body>
<main class="sheet">
  <section class="card card--front" aria-label="Business card front">
    <div class="brand">
      <span class="brand__dot"></span>
      <span class="brand__name">Verde<br>Nutrition</span>
    </div>
    <span class="divider"></span>
    <div class="details">
      <h1 class="details__name">Harriet Lowe</h1>
      <p class="details__role">Specialist Rehabilitation Dietitian</p>
      <ul class="contact">
        <li class="contact__item">
          <svg class="contact__icon" viewBox="0 0 24 24" aria-hidden="true"><path d="M6.6 10.8a15.1 15.1 0 0 0 6.6 6.6l2.2-2.2a1 1 0 0 1 1-.25 11.4 11.4 0 0 0 3.6.57 1 1 0 0 1 1 1V20a1 1 0 0 1-1 1A17 17 0 0 1 3 4a1 1 0 0 1 1-1h3.5a1 1 0 0 1 1 1c0 1.25.2 2.45.57 3.57a1 1 0 0 1-.25 1z"/></svg>
          07700900123
        </li>
        <li class="contact__item">
          <svg class="contact__icon" viewBox="0 0 24 24" aria-hidden="true"><path d="M2 5h20v14H2z" fill="none"/><path d="M2 5h20v1.5l-10 6.5L2 6.5zM2 8.5l10 6.5 10-6.5V19H2z"/></svg>
          harriet@verdenutrition.co.uk
        </li>
      </ul>
    </div>
  </section>

  <section class="card card--back" aria-label="Business card back">
    <p class="back-brand">Verde<br>Nutrition</p>
  </section>
</main>
</body>
</html>
```